Pictures to represent a consulting company and their main topics

We need around 10 pictures which can be used in blogs, webpages, powerpoints or articles to prettify and visualize the content.
We are a business consulting company in the financial industry.
We are based in and focussed on Switzerland.
Our main colours are blue turquise and grey (see www.veltrano.example).
The main topics, we would like to use the pictures for are:
- Digitalization
- Regulations
- Agile Project Management
- Advisory Process
- Automated System Testing
The price is for 10 pictures (which should be similar and therefore are not considered as 10 independent projects).
We propose to start with 3 example pictures to agree on the style. The rest will then be similar ones of the same style.
I have added examples from other companies.
It can be based on stock images or (prefferably) sketched images. Important is that the style is always the same.
Target Market(s)
Banking and Banking Consulting Market Switzerland
Industry/Entity Type
Business

```html
<!DOCTYPE html>
<html lang="en">
<head>
<meta charset="utf-8">
<title>Consulting Topic Cards</title>
<link rel="stylesheet" href="https://fonts.googleapis.com/css2?family=Bebas+Neue&family=Oswald:wght@500&display=swap">
<style>
  :root {
    --paper: #ffffff;
    --band-dark: #0e2f3b;
    --band-mid: #1c4756;
    --title: #ffffff;
    --stripe: rgba(255,255,255,0.16);
    --stripe-soft: rgba(255,255,255,0.08);
    --tone-deep: #1d4250;
    --tone-mid: #4f7787;
    --tone-light: #a9c4cd;
    --tone-pale: #d3e1e5;
  }
  * { margin: 0; padding: 0; box-sizing: border-box; }
  html, body { width: 1200px; height: 1200px; overflow: hidden; background: var(--paper); }
  .canvas { position: relative; width: 1200px; height: 1200px; }
  .card { position: absolute; width: 546px; height: 364px; overflow: hidden; }
  .card--advisory { left: 27px; top: 56px; }
  .card--testing { left: 597px; top: 56px; }
  .card--digital { left: 27px; top: 448px; }
  .card--regulations { left: 597px; top: 450px; }
  .card--agile { left: 301px; top: 835px; height: 335px; }
  .photo { position: absolute; left: 0; top: 0; width: 100%; height: calc(100% - 48px); }
  .photo--advisory {
    background:
      radial-gradient(ellipse 45% 40% at 70% 80%, rgba(211,225,229,0.7), transparent 70%),
      radial-gradient(ellipse 35% 50% at 88% 30%, rgba(169,196,205,0.6), transparent 70%),
      linear-gradient(115deg, var(--tone-deep) 0%, #3a6373 35%, #6b93a2 60%, #2a5060 100%);
  }
  .photo--testing {
    background:
      radial-gradient(ellipse 40% 55% at 30% 35%, rgba(40,70,82,0.75), transparent 70%),
      radial-gradient(ellipse 50% 35% at 60% 80%, rgba(29,66,80,0.7), transparent 70%),
      linear-gradient(180deg, #2c5261 0%, #7fa2ae 35%, var(--tone-pale) 62%, #8aaab5 80%, var(--tone-deep) 100%);
  }
  .photo--digital {
    background:
      radial-gradient(ellipse 30% 30% at 48% 48%, rgba(170,168,130,0.75), transparent 75%),
      radial-gradient(ellipse 55% 60% at 50% 60%, rgba(20,40,48,0.55), transparent 75%),
      linear-gradient(135deg, #17394a 0%, #3d6474 45%, #2b4e5c 70%, #15323f 100%);
  }
  .photo--regulations {
    background:
      radial-gradient(ellipse 28% 55% at 72% 60%, rgba(40,68,80,0.55), transparent 75%),
      linear-gradient(180deg, #7ea2b0 0%, var(--tone-light) 55%, #6a8d9b 78%, #3c5f6d 100%);
  }
  .photo--agile {
    background:
      radial-gradient(ellipse 40% 45% at 30% 70%, rgba(29,66,80,0.75), transparent 70%),
      radial-gradient(ellipse 40% 35% at 80% 70%, rgba(211,225,229,0.7), transparent 70%),
      linear-gradient(120deg, #203f4c 0%, var(--tone-mid) 45%, #9dbac4 75%, #6f94a2 100%);
  }
  .overlay { position: absolute; left: 0; top: 0; width: 100%; height: calc(100% - 48px); }
  .title { font-family: 'Bebas Neue', 'Oswald', sans-serif; fill: var(--title); }
  .band {
    position: absolute; left: 0; bottom: 0; width: 100%; height: 48px;
    background: linear-gradient(90deg, var(--band-dark), var(--band-mid));
    display: flex; align-items: center; justify-content: flex-end; padding-right: 26px;
  }
  .brand { display: flex; align-items: center; gap: 5px; color: var(--title);
    font-family: 'Oswald', sans-serif; font-weight: 500; font-size: 14px; letter-spacing: 1px; }
  .brand-mark { width: 9px; height: 9px; background: var(--title); }
</style>
</head>
<body>
<div class="canvas">

  <section class="card card--advisory">
    <div class="photo photo--advisory" role="img" aria-label="Photo of two business people in suits working together at a desk with a keyboard, blue-toned"></div>
    <svg class="overlay" viewBox="0 0 546 316" preserveAspectRatio="none">
      <rect x="0" y="108" width="546" height="14" fill="var(--stripe)"/>
      <rect x="0" y="150" width="546" height="24" fill="var(--stripe-soft)"/>
      <rect x="0" y="174" width="546" height="8" fill="var(--stripe)"/>
      <text class="title" x="34" y="166" font-size="76" textLength="247" lengthAdjust="spacingAndGlyphs">ADVISORY</text>
      <text class="title" x="34" y="200" font-size="40" textLength="247" lengthAdjust="spacing">PROCESS</text>
    </svg>
    <div class="band"><span class="brand"><span class="brand-mark"></span>VELTRANO</span></div>
  </section>

  <section class="card card--testing">
    <div class="photo photo--testing" role="img" aria-label="Photo of a person at a whiteboard in a lab with colourful test cables on a desk, blue-toned"></div>
    <svg class="overlay" viewBox="0 0 546 316" preserveAspectRatio="none">
      <rect x="0" y="82" width="546" height="10" fill="var(--stripe)"/>
      <rect x="0" y="112" width="546" height="20" fill="var(--stripe-soft)"/>
      <rect x="0" y="136" width="546" height="8" fill="var(--stripe)"/>
      <text class="title" x="233" y="130" font-size="66" textLength="269" lengthAdjust="spacingAndGlyphs">AUTOMATED</text>
      <text class="title" x="233" y="160" font-size="34" textLength="269" lengthAdjust="spacing">SYSTEM TESTING</text>
    </svg>
    <div class="band"><span class="brand"><span class="brand-mark"></span>VELTRANO</span></div>
  </section>

  <section class="card card--digital">
    <div class="photo photo--digital" role="img" aria-label="Photo of hands holding a tablet that shows warehouse shelves with boxes and order pick time labels, blue-toned"></div>
    <svg class="overlay" viewBox="0 0 546 316" preserveAspectRatio="none">
      <rect x="0" y="46" width="546" height="10" fill="var(--stripe)"/>
      <rect x="0" y="76" width="546" height="18" fill="var(--stripe-soft)"/>
      <rect x="0" y="96" width="546" height="6" fill="var(--stripe)"/>
      <text class="title" x="199" y="94" font-size="66" textLength="294" lengthAdjust="spacingAndGlyphs">DIGITALIZATION</text>
    </svg>
    <div class="band"><span class="brand"><span class="brand-mark"></span>VELTRANO</span></div>
  </section>

  <section class="card card--regulations">
    <div class="photo photo--regulations" role="img" aria-label="Photo of two tall stacks of document binders on a wooden floor in an office room, blue-toned"></div>
    <svg class="overlay" viewBox="0 0 546 316" preserveAspectRatio="none">
      <rect x="0" y="140" width="546" height="12" fill="var(--stripe)"/>
      <rect x="0" y="172" width="546" height="22" fill="var(--stripe-soft)"/>
      <rect x="0" y="196" width="546" height="6" fill="var(--stripe)"/>
      <text class="title" x="41" y="194" font-size="72" textLength="314" lengthAdjust="spacingAndGlyphs">REGULATIONS</text>
    </svg>
    <div class="band"><span class="brand"><span class="brand-mark"></span>VELTRANO</span></div>
  </section>

  <section class="card card--agile">
    <div class="photo photo--agile" role="img" aria-label="Photo of a team meeting around a conference table with a presenter in the foreground, blue-toned"></div>
    <svg class="overlay" viewBox="0 0 546 287" preserveAspectRatio="none">
      <rect x="0" y="150" width="546" height="14" fill="var(--stripe-soft)"/>
      <rect x="0" y="166" width="546" height="8" fill="var(--stripe)"/>
      <text class="title" x="34" y="174" font-size="104" textLength="194" lengthAdjust="spacingAndGlyphs">AGILE</text>
      <text class="title" x="34" y="201" font-size="28" textLength="194" lengthAdjust="spacingAndGlyphs">PROJECT MANAGEMENT</text>
    </svg>
    <div class="band"><span class="brand"><span class="brand-mark"></span>VELTRANO</span></div>
  </section>

</div>
</body>
</html>
```